Cedar Lantern Roots Gathering Music Conference & Concert Series needs a banner design to welco...

We are looking for a banner to use as a backdrop where people can take pictures and promote the event as they upload to social media. The music conference primarily targets high school students so we are looking for a design that will attract a younger audience. The festival revolves around music appreciation in the US/Mexico border. We like the "Cedar LanternRoots Gathering" trumpet logo on the "5th annual" design attached, but we are open to other designs.
Target Market(s)
ages 15-45
Colors
Designer to choose colors to be used in the design.
Look and feel

```html
<!DOCTYPE html>
<html lang="en">
<head>
<meta charset="utf-8">
<title>Cedar Lantern Roots Gathering — Banner</title>
<link rel="stylesheet" href="https://fonts.googleapis.com/css2?family=Oswald:wght@500;600&family=Open+Sans:wght@400&display=swap">
<style>
  :root {
    --backdrop: #d4d5d6;
    --navy-deep: #0d2a63;
    --navy: #1d4f9c;
    --navy-glow: #2f6bb8;
    --orange: #f4982a;
    --red: #c4213a;
    --green: #1f7a3c;
    --white: #ffffff;
    --straw: #c9a46a;
    --serape: #b8402e;
  }
  * { margin: 0; padding: 0; box-sizing: border-box; }
  html, body {
    width: 1200px;
    height: 666px;
    overflow: hidden;
    background: var(--backdrop);
  }
  .banner {
    position: absolute;
    left: 79px;
    top: 71px;
    width: 1047px;
    height: 524px;
    overflow: hidden;
    background:
      radial-gradient(ellipse 60% 70% at 52% 62%, var(--navy-glow) 0%, var(--navy) 45%, var(--navy-deep) 100%);
  }
  .festive-still-life {
    position: absolute;
    left: 0;
    top: 0;
    width: 270px;
    height: 225px;
    background: linear-gradient(135deg, var(--straw) 0%, #d9b57a 35%, var(--serape) 65%, #e07a2c 100%);
    clip-path: polygon(0 0, 100% 0, 92% 30%, 60% 55%, 30% 85%, 0 100%);
  }
  .bunting {
    position: absolute;
    left: 550px;
    top: 0;
    width: 497px;
    height: 150px;
    background: linear-gradient(90deg, var(--orange) 0%, var(--red) 35%, var(--green) 60%, var(--red) 80%, var(--orange) 100%);
    clip-path: polygon(0 0, 100% 0, 100% 90%, 92% 100%, 40% 55%, 0 30%);
    opacity: 0.9;
  }
  .edition {
    position: absolute;
    left: 356px;
    top: 146px;
    font-family: "Oswald", sans-serif;
    font-weight: 600;
    font-size: 33px;
    line-height: 1;
    color: var(--white);
    letter-spacing: 0.5px;
    white-space: nowrap;
  }
  .rule {
    position: absolute;
    height: 5px;
    background: var(--green);
  }
  .rule--top { left: 345px; top: 189px; width: 550px; }
  .rule--side { left: 154px; top: 344px; width: 102px; }
  .wordmark {
    font-weight: normal;
  }
  .wordmark__main {
    position: absolute;
    left: 0;
    top: 208px;
    width: 1047px;
    text-align: center;
    font-family: "Oswald", sans-serif;
    font-weight: 500;
    font-size: 92px;
    line-height: 1;
    letter-spacing: 1px;
    white-space: nowrap;
    color: var(--orange);
    text-shadow: 0 4px 8px rgba(0, 0, 0, 0.35);
  }
  .wordmark__accent { color: var(--red); }
  .wordmark__sub {
    position: absolute;
    left: 345px;
    top: 304px;
    font-family: "Open Sans", sans-serif;
    font-weight: 400;
    font-size: 76px;
    line-height: 1;
    letter-spacing: 4px;
    white-space: nowrap;
    color: var(--green);
  }
  .tagline {
    position: absolute;
    left: 372px;
    top: 396px;
    font-family: "Oswald", sans-serif;
    font-weight: 600;
    font-size: 25px;
    line-height: 1;
    color: var(--white);
    letter-spacing: 0.3px;
    white-space: nowrap;
  }
</style>
</head>
<body>
  <main class="banner">
    <div class="festive-still-life" role="img" aria-label="Photo of a straw sombrero, striped serape blanket and maracas"></div>
    <div class="bunting" role="img" aria-label="String of orange, red and green papel picado flags"></div>

    <p class="edition">5TH ANNUAL</p>
    <div class="rule rule--top"></div>

    <h1 class="wordmark">
      <span class="wordmark__main">Cedar Lantern<span class="wordmark__accent">Roots</span></span>
      <span class="wordmark__sub">Gathering</span>
    </h1>
    <div class="rule rule--side"></div>

    <p class="tagline">MUSIC CONFERENCE &amp; CONCERT SERIES</p>
  </main>
</body>
</html>
```